Business Card Design

Recruitment Company. Want to keep the logo and the green colour

Industry/Entity Type

Business

Contact Information for Business Card

Hi,

1.)
MARTIN HOLLOWAY
Director
Level 6, 248 Finch Street
Brisbane QLD 4000
M 0412 630 574
E martin@tallonstaffing.com.au
www.tallonstaffing.com.au

2.)
TOM WAVERLEY
Director
Level 6, 248 Finch Street
Brisbane QLD 4000
M 0419 247 613
E tom@tallonstaffing.com.au

Want something different and eye catching, happy for you guys to use your design flare to work some magic with these.

Many Thanks
Tom

```html
<!DOCTYPE html>
<html lang="en">
<head>
<meta charset="utf-8">
<title>Tallon Staffing — Business Cards</title>
<link href="https://fonts.googleapis.com/css2?family=Michroma&display=swap" rel="stylesheet">
<style>
  :root {
    --slate: #27323c;
    --sky: #4a9fd4;
    --white: #ffffff;
  }
  html, body {
    margin: 0;
    padding: 0;
    overflow: hidden;
  }
  .canvas {
    position: relative;
    width: 1200px;
    height: 982px;
    background: var(--slate);
    font-family: "Michroma", sans-serif;
    color: var(--white);
    overflow: hidden;
  }
  .brand {
    position: absolute;
    top: 178px;
    display: flex;
    align-items: center;
    gap: 12px;
    font-size: 26px;
    letter-spacing: 3px;
  }
  .brand-mark {
    width: 18px;
    height: 18px;
  }
  .brand--left { left: 80px; color: var(--sky); }
  .brand--left .brand-mark { background: var(--sky); }
  .brand--right { right: 80px; color: var(--white); }
  .brand--right .brand-mark { background: var(--white); }

  .person {
    position: absolute;
    top: 228px;
    line-height: 1;
  }
  .person--left { right: 633px; text-align: right; }
  .person--right { left: 611px; text-align: left; }
  .person-name {
    font-size: 31px;
    letter-spacing: 4px;
    margin: 0 0 20px;
  }
  .person-name span { display: block; margin-bottom: 20px; }
  .person-role {
    font-size: 23px;
    letter-spacing: 3px;
    margin: 0 0 14px;
  }
  .person--left .person-name { color: var(--sky); }
  .person--left .person-role { color: var(--white); }
  .person--right .person-name { color: var(--white); }
  .person--right .person-role { color: var(--sky); }

  .contact {
    position: absolute;
    top: 540px;
    width: 490px;
  }
  .contact--left { left: 87px; }
  .contact--right { left: 613px; }
  .street {
    margin: 0;
    line-height: 1;
    white-space: nowrap;
    display: flex;
    align-items: baseline;
    gap: 14px;
  }
  .street-number, .street-suffix { font-size: 30px; letter-spacing: 4px; }
  .street-name { font-size: 48px; letter-spacing: 3px; }
  .city {
    margin: 28px 0 24px;
    font-size: 50px;
    letter-spacing: 5px;
    color: var(--sky);
    line-height: 1;
  }
  .details {
    margin: 0;
    font-size: 16px;
    letter-spacing: 2px;
    line-height: 36px;
    white-space: nowrap;
  }
</style>
</head>
<body>
<main class="canvas">
  <div class="brand brand--left"><span class="brand-mark"></span>TALLON</div>
  <div class="brand brand--right"><span class="brand-mark"></span>TALLON</div>

  <section class="person person--left">
    <h1 class="person-name"><span>MARTIN</span>HOLLOWAY</h1>
    <p class="person-role">DIRECTOR</p>
    <p class="person-role">LEVEL SIX</p>
  </section>

  <section class="person person--right">
    <h1 class="person-name"><span>TOM</span>WAVERLEY</h1>
    <p class="person-role">DIRECTOR</p>
    <p class="person-role">LEVEL SIX</p>
  </section>

  <address class="contact contact--left">
    <p class="street"><span class="street-number">248</span><span class="street-name">FINCH</span><span class="street-suffix">ST</span></p>
    <p class="city">BRISBANE</p>
    <p class="details">QLD 4000 M 0412 630 574 E<br>MARTIN@TALLONSTAFFING.COM.AU<br>WWW.TALLONSTAFFING.COM.AU</p>
  </address>

  <address class="contact contact--right">
    <p class="street"><span class="street-number">248</span><span class="street-name">FINCH</span><span class="street-suffix">ST</span></p>
    <p class="city">BRISBANE</p>
    <p class="details">QLD 4000 M 0419 247 613 E<br>TOM@TALLONSTAFFING.COM.AU<br>WWW.TALLONSTAFFING.COM.AU</p>
  </address>
</main>
</body>
</html>
```